Two Wine Labels, One Red One White

We are looking to create a brand image for our wines. There are two requirements by law that we need, however beyond that, the creativity comes from the designer. Required are:
On The Red Label, Alcohol 14.1White Label Alcohol 12.5, The Size, 750ML
SO One label for the red wine with alcohol at 14.1 in a 750 ML Bottle, and one Label for white with alcohol at 12.5 in a 750 ML bottle.

Hi All:
I have some more clarity to assist in the design work.
The Brand Name of the wine is Valmaren for both the red and the white
The name should appear as Valmaren with the Brackets around phonetical as seen here
[vahl-mah-ren] Both the word and the phonetical spelling should appear.
and can be seen on wordplenk.com The Brand Name text can be black
Label should be very light grey, I am trying to capture a Stone grey or texture from stone, although, NOT Marble.
The Red Label, The word "Red" should be in red
The White Label, The word "White" should be in White, all the original remaining elements remain as originally posted.

I look forward to hearing from you for any additional questions.
Updates

Just added a logo Not really seeing what we are trying to achieve, maybe using the logo in the design may assist

Target Market(s)

Wine Aficionados

Requirements
Must have
• Details described in Project Description above, these are required by law. The Name of the Brand will be posted shortly. For the moment if you take the project, just place red on one label and white on the other.
Nice to have
• These two wines are from California (USA), so the Sierra Nevada Mountains could be an inspiration, to outline of California or coast line, a vineyard (of course), a vine...We are in silicon valley, so there is a map of silicon valley with the Bay and ocean, something from a map could work, or let your creativity flow and not use any of these concepts.
Should not have
• I do not not care for decorative fonts, however all else is open

```html
<!DOCTYPE html>
<html lang="en">
<head>
<meta charset="utf-8">
<title>Valmaren Wine Labels</title>
<link href="https://fonts.googleapis.com/css2?family=Questrial&family=PT+Sans&display=swap" rel="stylesheet">
<style>
  :root {
    --page: #ffffff;
    --stone-light: #e4e3e0;
    --stone-mid: #d6d5d2;
    --stone-shade: #cbcac7;
    --ink-dark: #141213;
    --ink-light: #ffffff;
    --red-accent: #ec1c24;
    --white-accent: #d7e021;
  }
  * { margin: 0; padding: 0; box-sizing: border-box; }
  html, body {
    width: 1200px;
    height: 900px;
    overflow: hidden;
    background: var(--page);
  }
  .canvas {
    position: relative;
    width: 1200px;
    height: 900px;
    background: var(--page);
  }
  .label {
    position: absolute;
    top: 142px;
    width: 444px;
    height: 618px;
    background:
      radial-gradient(ellipse at 25% 20%, var(--stone-light) 0%, transparent 60%),
      radial-gradient(ellipse at 80% 85%, var(--stone-shade) 0%, transparent 55%),
      linear-gradient(160deg, var(--stone-light) 0%, var(--stone-mid) 50%, var(--stone-shade) 100%);
    color: var(--ink-dark);
    text-align: center;
  }
  .label--red { left: 134px; }
  .label--white { left: 622px; }

  .label__scene {
    position: absolute;
    left: -1px;
    top: 75px;
    width: 446px;
    height: 204px;
  }
  .label--red .label__scene {
    background:
      linear-gradient(180deg,
        #39b6ea 0%, #4cc3f0 18%,
        #b83a3a 34%, #d8562e 48%, #e48a3e 58%,
        #2f86c8 66%, #3a8fd0 78%,
        #d0702e 90%, #c25a28 100%);
  }
  .label--white .label__scene {
    background:
      linear-gradient(180deg,
        #5b93bf 0%, #6aa2c8 18%,
        #8a5a44 34%, #b0784a 48%, #c8955e 58%,
        #3a6cae 66%, #4678b4 78%,
        #c08a4a 90%, #a87040 100%);
  }

  .label__brand {
    position: absolute;
    left: 0;
    right: 0;
    top: 306px;
    font-family: "Questrial", "Century Gothic", sans-serif;
    font-size: 62px;
    line-height: 1;
    font-weight: 400;
    color: var(--ink-dark);
  }
  .label__phonetic {
    position: absolute;
    left: 0;
    right: 0;
    top: 376px;
    font-family: "Questrial", "Century Gothic", sans-serif;
    font-size: 30px;
    line-height: 1;
  }
  .label--red .label__phonetic { color: var(--red-accent); }
  .label--white .label__phonetic { color: #a8b010; }

  .label__variety {
    position: absolute;
    left: 0;
    top: 421px;
    width: 444px;
    height: 65px;
    font-family: "PT Sans", "Myriad Pro", sans-serif;
    font-size: 76px;
    line-height: 68px;
    color: var(--ink-light);
    white-space: nowrap;
    overflow: hidden;
    text-align: left;
  }
  .label--red .label__variety {
    background: var(--red-accent);
    letter-spacing: 48px;
    padding-left: 103px;
  }
  .label--white .label__variety {
    background: var(--white-accent);
    letter-spacing: 44px;
    padding-left: 14px;
  }

  .label__legal {
    position: absolute;
    left: 0;
    right: 0;
    top: 536px;
    font-family: "PT Sans", "Myriad Pro", sans-serif;
    font-size: 21px;
    line-height: 34px;
    color: var(--ink-dark);
  }
</style>
</head>
<body>
<main class="canvas">
  <section class="label label--red">
    <div class="label__scene" role="img" aria-label="Painted landscape of red and orange mountains beside a blue lake under a bright sky"></div>
    <h1 class="label__brand">Valmaren</h1>
    <p class="label__phonetic">[vahl-mah-ren]</p>
    <p class="label__variety">RED</p>
    <p class="label__legal">Alcohol 14.1<br>750мл.</p>
  </section>

  <section class="label label--white">
    <div class="label__scene" role="img" aria-label="Painted landscape of muted tan mountains beside a blue lake under a soft sky"></div>
    <h1 class="label__brand">Valmaren</h1>
    <p class="label__phonetic">[vahl-mah-ren]</p>
    <p class="label__variety">WHITE</p>
    <p class="label__legal">Alcohol 12.5<br>750мл.</p>
  </section>
</main>
</body>
</html>
```